New Website Design (Uncoded) Competition for Lorvex Trade Link

Please submit design concepts for a Joomla 3.0 Website for LORVEX TRADE LINK company. Our client prefers a modem style design, responsive to all mobile devices,
The website demo content needs to be clear and detailed.

Menu sample:
Home/About Us/Service/Strength/Partner/News/Contact US/Blog

Requirements:
1. Only need to submit the PSD for the design, coding work is not included.
2. Please submit both Homepage and Inner page to demonstrate the concept.
3. The Homepage needs to include: LOGO/MENU/Banner/Language Switcher/Company Introduction/Welcome module/Advertising Module/Footer Menu/Footer/Copyright/Social Links
4. Use Asian business women for demo pictures/Could try city pictures for background.
5. Prefer SINGLE SCREEN design rather than scrollable multiple screen designs.
6. Avoid any chain symbol since the company is more about financial business.
7. Avoid any direct connotations related with money or cash.
Updates

Hi Designers, I have clearly state the requirements that avoid using neg connontation pictures like cash/ property, though still receive concepts like that. Please check the brief clearly and mark at Update with "cheers" Kel from VT

Target Market(s)

Dongrui Lorvex Trade link Company provide cross-border Supply chain Financial service by integrating Dongrui Trade Link resource.
The Company mission is become the most respectful, professional and valuable Chinese Supply Chain Financial Company, pioneer the supply chain industry.

Industry/Entity Type

Financial

Font styles to use
Sans Serif

Colors
33b7a4

Requirements
Must have
• 1. Necessary Web element, including Logo/navigation/ Banner/ Footer
2. Asia business Women pictures.
Should not have
• 6. Avoid any chain symbol since the company is more about financial business.

```html
<!DOCTYPE html>
<html lang="en">
<head>
<meta charset="utf-8">
<title>Lorvex Trade Link</title>
<link href="https://fonts.googleapis.com/css2?family=Roboto:wght@300;400;500;700&display=swap" rel="stylesheet">
<style>
  :root {
    --header-bg: #f7f7f7;
    --ink: #111111;
    --nav-ink: #1a1a1a;
    --muted: #8a8a8a;
    --brand: #1b7ec2;
    --brand-mark: #3aa6dc;
    --logo-ink: #5a5a5a;
    --map-light: #ffffff;
    --map-blue: #dce9f6;
    --button: #5c5c5c;
    --button-ink: #ffffff;
    --footer-bg: #ffffff;
    --footer-line: #e4e4e4;
    --icon: #7a7a7a;
  }
  * { box-sizing: border-box; margin: 0; padding: 0; }
  html, body { width: 1200px; height: 754px; overflow: hidden; }
  body { font-family: "Roboto", Arial, sans-serif; color: var(--ink); background: var(--map-light); position: relative; }

  .site-header {
    position: absolute; top: 0; left: 0; width: 1200px; height: 67px;
    background: var(--header-bg); z-index: 2;
  }
  .brand { position: absolute; left: 161px; top: 14px; display: flex; align-items: center; gap: 10px; }
  .brand-square { width: 22px; height: 22px; background: var(--brand-mark); }
  .brand-name {
    font-weight: 700; font-size: 15px; line-height: 17px; color: var(--logo-ink);
    letter-spacing: 0.5px; width: 110px;
  }
  .main-nav { position: absolute; left: 380px; top: 24px; display: flex; gap: 18px; }
  .main-nav a {
    font-size: 14px; font-weight: 700; color: var(--nav-ink); text-decoration: none; letter-spacing: 0.1px;
  }
  .lang-switch {
    position: absolute; left: 943px; top: 25px; font-size: 12px; font-weight: 300; color: var(--muted);
    display: flex; align-items: center; gap: 4px;
  }

  .hero { position: absolute; top: 67px; left: 0; width: 1200px; height: 628px; }
  .hero-map {
    position: absolute; inset: 0;
    background: linear-gradient(160deg, var(--map-light) 0%, var(--map-light) 18%, #eef4fb 40%, var(--map-blue) 65%, var(--map-blue) 100%);
  }
  .hero-content { position: absolute; left: 150px; width: 900px; top: 0; text-align: center; }
  .hero-title { position: absolute; top: 97px; width: 100%; font-size: 35px; font-weight: 500; letter-spacing: -0.3px; }
  .hero-title span { color: var(--brand); }
  .hero-intro {
    position: absolute; top: 172px; width: 100%; font-size: 22.5px; font-weight: 300; line-height: 28px;
  }
  .divider {
    position: absolute; top: 318px; left: 11px; width: 878px; height: 0;
    border-top: 2px dotted #222;
  }
  .hero-note {
    position: absolute; top: 361px; width: 100%; font-size: 21px; font-weight: 300; line-height: 28px;
  }
  .hero-note a { color: inherit; text-decoration: underline; text-underline-offset: 3px; }
  .join-button {
    position: absolute; top: 466px; left: 279px; width: 341px; height: 70px;
    background: var(--button); color: var(--button-ink); border-radius: 3px;
    font-size: 35px; font-weight: 300; line-height: 70px; text-decoration: none; text-align: center;
  }

  .site-footer {
    position: absolute; top: 695px; left: 0; width: 1200px; height: 59px;
    background: var(--footer-bg); border-top: 1px solid var(--footer-line);
  }
  .copyright { position: absolute; left: 150px; top: 22px; font-size: 12px; font-weight: 300; color: var(--muted); }
  .copyright a { color: var(--brand); text-decoration: none; }
  .copyright .sep { margin: 0 5px; }
  .social { position: absolute; left: 957px; top: 19px; display: flex; gap: 16px; }
  .social a { display: block; width: 21px; height: 21px; border: 2px solid var(--icon); border-radius: 50%; }
</style>
</head>
<body>
  <header class="site-header">
    <div class="brand">
      <span class="brand-square"></span>
      <span class="brand-name">LORVEX TRADE LINK</span>
    </div>
    <nav class="main-nav">
      <a href="#">ABOUT US</a>
      <a href="#">SERVICE</a>
      <a href="#">STRENGTH</a>
      <a href="#">PARTNER</a>
      <a href="#">NEWS</a>
      <a href="#">CONTACT US</a>
      <a href="#">BLOG</a>
    </nav>
    <div class="lang-switch">Choose Language
      <svg width="10" height="6" viewBox="0 0 10 6"><path d="M1 1l4 4 4-4" fill="none" stroke="#8a8a8a" stroke-width="1.2"/></svg>
    </div>
  </header>

  <main class="hero">
    <div class="hero-map" role="img" aria-label="Faint light-blue map of a coastal delta region in the background"></div>
    <div class="hero-content">
      <h1 class="hero-title">Welcome to <span>Lorvex Trade Link</span></h1>
      <p class="hero-intro">Consectetur adipiscing elit. In ac turpis nulla. Nulla eget viverra nunc, quis pretium massa<br>Morbi vestibulum ante eget enim porttitor suscipit. Integer nunc quam, pharetra<br>Praesent et enim vitae ex rhoncus semper. Mauris faucibus ligula mauris.<br>Vivamus lobortis in eros quis mattis.</p>
      <div class="divider"></div>
      <p class="hero-note">Nunc pharetra sollicitudin tellus ut sagittis. <a href="#">Nunc odio mi</a>, consectetur eget rutrum ac, pulvinar a eros.<br>Nullam in tellus sit amet nunc egestas elementum eu eget ligula.</p>
      <a class="join-button" href="#">Free to Join Us</a>
    </div>
  </main>

  <footer class="site-footer">
    <p class="copyright">©2014 Lorvex Trade Link. All Rights Reserved. <a href="#">Privacy Policy</a><span class="sep">|</span><a href="#">News</a><span class="sep">|</span><a href="#">Contact Us</a></p>
    <div class="social">
      <a href="#" aria-label="Social link one"></a>
      <a href="#" aria-label="Social link two"></a>
      <a href="#" aria-label="Social link three"></a>
    </div>
  </footer>
</body>
</html>
```